Velvet corsaro

I want a business card design. the company is an infrastructure development company.

Target Market(s)

Government
real estate investors
real estate clients

Industry/Entity Type

Business

```html
<!DOCTYPE html>
<html lang="en">
<head>
<meta charset="utf-8">
<title>Velvet Corsaro — Business Card</title>
<link href="https://fonts.googleapis.com/css2?family=Open+Sans:wght@400;600;700&display=swap" rel="stylesheet">
<style>
  :root {
    --backdrop-light: #e6f4fc;
    --backdrop-dark: #6fc0ec;
    --navy: #222d42;
    --band-grey: #c6c6c6;
    --band-shadow: #8d8f94;
    --accent-blue: #1e9bd7;
    --accent-red: #e8333b;
    --white: #ffffff;
    --ink: #2a3347;
    --card-edge: #6b6f78;
  }
  html, body {
    margin: 0;
    padding: 0;
    width: 1200px;
    height: 1000px;
    overflow: hidden;
  }
  body {
    background: radial-gradient(ellipse 70% 75% at 50% 50%, var(--backdrop-light) 0%, #bfe3f7 45%, var(--backdrop-dark) 100%);
    font-family: "Open Sans", sans-serif;
    position: relative;
  }
  .business-card {
    position: absolute;
    left: 270px;
    top: 316px;
    width: 661px;
    height: 367px;
    background: var(--white);
    box-shadow: 0 0 0 1px var(--card-edge);
    overflow: hidden;
  }
  .card-bands {
    position: absolute;
    left: 0;
    top: 0;
    width: 661px;
    height: 235px;
  }
  .brand-name {
    position: absolute;
    left: 34px;
    top: 76px;
    display: flex;
    align-items: center;
    gap: 12px;
    color: var(--white);
    font-weight: 600;
    font-size: 27px;
    line-height: 32px;
    letter-spacing: 1px;
    text-transform: uppercase;
  }
  .brand-mark {
    width: 22px;
    height: 22px;
    background: var(--accent-red);
    flex: none;
  }
  .contact-person {
    position: absolute;
    left: 343px;
    top: 44px;
    color: var(--white);
  }
  .person-name {
    margin: 0 0 4px;
    font-size: 29px;
    font-weight: 700;
    color: var(--accent-blue);
    line-height: 40px;
  }
  .person-details {
    margin: 0;
    font-size: 17px;
    line-height: 25.5px;
    font-weight: 400;
  }
  .company-details {
    position: absolute;
    left: 0;
    top: 254px;
    width: 661px;
    text-align: center;
    color: var(--ink);
    font-size: 18px;
    line-height: 27.5px;
  }
  .company-details p { margin: 0; }
  .company-details .web { text-decoration: underline; }
</style>
</head>
<body>
  <section class="business-card">
    <svg class="card-bands" viewBox="0 0 661 235" aria-hidden="true">
      <rect x="0" y="0" width="661" height="235" fill="var(--band-grey)"/>
      <polygon points="0,6 220,22 661,6 661,205 442,228 0,205" fill="var(--band-shadow)"/>
      <polygon points="0,6 220,22 661,6 661,222 442,204 0,224" fill="var(--navy)"/>
      <polygon points="0,0 661,0 661,6 220,22 0,6" fill="var(--band-grey)"/>
      <polygon points="0,224 442,204 661,222 661,229 0,229" fill="var(--band-grey)"/>
    </svg>

    <div class="brand-name">
      <span class="brand-mark"></span>
      <span>Velvet<br>Corsaro</span>
    </div>

    <div class="contact-person">
      <h1 class="person-name">Tunde Adeyemi</h1>
      <p class="person-details">
        MD.<br>
        +234 8014472208,<br>
        +234 7031865524<br>
        tunde@velvetcorsaro.com
      </p>
    </div>

    <div class="company-details">
      <p>12, Marula street, Off Harbour Link Road, Ikeja Lagos, Nigeria</p>
      <p>+234 12657041, +234 7052918836</p>
      <p>info@velvetcorsaro.com <span class="web">www.velvetcorsaro.com</span></p>
    </div>
  </section>
</body>
</html>
```